Brochure Design Project

We are looking for a brochure to communicate the various different program we offer within the "Trail & Habitat Studies" department
( www.fieldtrek.rv82.qz.ca )
We have a large photo bank of students engaged in our programs and can willingly provide them if requested.

Target Market(s)

parents, students, academics, administrators

Industry/Entity Type

Bank

Requirements
Must have
• nature based theme. adventure and ecology.

```html
<!DOCTYPE html>
<html lang="en">
<head>
<meta charset="utf-8">
<title>Trail &amp; Habitat Studies — Program Brochure</title>
<link href="https://fonts.googleapis.com/css2?family=Roboto+Slab:wght@700&family=Quicksand:wght@400;500;600&display=swap" rel="stylesheet">
<style>
:root{
  --bg:#2b2b2b;
  --green:#3f9a3a;
  --green-dark:#2d7a2c;
  --green-deep:#22602a;
  --slate:#3d5450;
  --slate-dark:#2c3b3a;
  --teal-strip:#4f7d72;
  --red-strip:#a0392c;
  --yellow-strip:#e3c43a;
  --white:#ffffff;
  --photo-sun:#c98a2a;
  --photo-map:#cfc8b4;
  --photo-hands:#b98766;
}
*{box-sizing:border-box;margin:0;padding:0}
html,body{width:1200px;height:1000px;overflow:hidden;background:var(--bg)}
body{font-family:"Quicksand",sans-serif;color:var(--white);position:relative}
.spread{position:absolute;left:190px;width:820px;height:450px;display:flex;box-shadow:0 6px 18px rgba(0,0,0,.5)}
.spread--outside{top:28px}
.spread--inside{top:520px}
.panel{position:relative;width:33.333%;height:100%;overflow:hidden}
h2{font-family:"Roboto Slab",serif;font-weight:700;font-size:13px;line-height:1.2}
p,li{font-size:8.2px;line-height:1.38}
.photo{display:block;width:100%}

/* outside: flap */
.panel--flap{background:linear-gradient(180deg,var(--slate) 0%,var(--slate-dark) 100%)}
.panel--flap .photo{height:178px;background:linear-gradient(135deg,#e7d9c6 0%,var(--photo-hands) 55%,#7a5a44 100%)}
.flap-curve{position:absolute;left:0;top:140px;width:100%;height:60px}
.brand-badge{position:absolute;right:12px;top:150px;display:flex;align-items:center;gap:4px;background:var(--white);padding:4px 6px;color:var(--slate-dark);font-size:8px;font-weight:600}
.brand-badge .mark{width:10px;height:10px;background:var(--green-dark)}
.flap-body{position:absolute;left:18px;right:16px;top:205px}
.flap-body h3{font-size:9.5px;font-weight:600;font-style:italic;text-align:center;margin-bottom:10px}
.flap-body p{font-style:italic;text-indent:12px}
.flap-body .byline{margin-top:8px;text-indent:0}

/* outside: research */
.panel--research{background:linear-gradient(180deg,var(--green) 0%,var(--green-dark) 100%);padding:14px 16px}
.panel--research h2{margin-bottom:6px}
.panel--research .lead{font-size:10px;text-align:center;margin-bottom:8px}
.panel--research .note{font-size:10px;margin-top:12px;line-height:1.25}
.panel--research .url{font-size:10px;text-align:center;margin-top:8px}
.partner{margin-top:14px;text-align:center;font-size:14px;font-weight:500;color:var(--white)}
.grass{position:absolute;left:0;bottom:0;width:100%;height:50px;background:linear-gradient(180deg,rgba(90,170,60,0) 0%,#3c8d2a 60%,#2e7321 100%)}

/* outside: ways */
.panel--ways{background:linear-gradient(160deg,var(--slate) 0%,var(--slate-dark) 100%);padding:14px 14px}
.panel--ways h2{margin-bottom:8px}
.panel--ways ul{list-style:none}
.panel--ways li{padding-left:10px;position:relative}
.panel--ways li::before{content:"·";position:absolute;left:2px}
.panel--ways p{margin-bottom:2px}
.circles{position:absolute;left:22px;bottom:16px;width:230px;height:78px}

/* inside */
.panel--program{background:var(--green-dark)}
.strip{height:9px}
.strip--teal{background:var(--teal-strip)}
.strip--red{background:var(--red-strip)}
.strip--yellow{background:var(--yellow-strip)}
.program-head{height:108px;background:linear-gradient(135deg,var(--green) 0%,var(--green-dark) 100%);padding:12px 14px}
.program-head h2{margin-bottom:8px}
.quote{font-size:8px}
.quote-by{font-size:10px;margin-bottom:3px}
.panel--program .photo{height:162px}
.photo--sun{background:radial-gradient(circle at 20% 20%,#f5d46a 0%,var(--photo-sun) 35%,#3a3a22 100%)}
.photo--dusk{background:linear-gradient(180deg,#7c7a70 0%,#d08c46 55%,#2a2a28 100%)}
.photo--map{background:linear-gradient(135deg,var(--photo-map) 0%,#b89f86 60%,#8f7c68 100%)}
.program-body{padding:12px 14px;border-top:3px solid var(--white)}
.program-body p{text-indent:10px}
.mini-brand{position:absolute;left:112px;bottom:10px;display:flex;align-items:center;gap:4px;background:var(--white);padding:3px 6px;color:var(--green-deep);font-size:9px;font-weight:600}
.mini-brand .mark{width:8px;height:8px;background:var(--green-deep)}
</style>
</head>
<body>

<section class="spread spread--outside" aria-label="Brochure outside">
  <article class="panel panel--flap">
    <div class="photo" role="img" aria-label="Photo of linked hands and forearms held together outdoors"></div>
    <svg class="flap-curve" viewBox="0 0 273 60" preserveAspectRatio="none" aria-hidden="true">
      <path d="M0 60 C80 20 180 10 273 0 L273 60 Z" fill="var(--slate)"/>
      <path d="M0 60 C80 22 180 12 273 2" fill="none" stroke="var(--green)" stroke-width="3"/>
    </svg>
    <div class="brand-badge"><span class="mark"></span>Ridgeline Academy</div>
    <div class="flap-body">
      <h3>Trail &amp; Habitat Studies Department (RV82)</h3>
      <p>The Trail &amp; Habitat Studies Department is dedicated to providing students with educational opportunities that reinforce their connection to the natural world and foster sustainability. We focus on giving students the necessary skills to think critically about personal choices and the relationships between society, economy, culture and the environment. Through action leadership, skill development and inspired experience, our students are empowered to make positive change in their communities. We offer numerous programs and have highlighted a few in this document.</p>
      <p>"The Trail &amp; Habitat Programs in River Valley District 82 help to fill a huge void in modern society: the void between what's taught in the classroom and the day-to-day miracles happening outside.</p>
      <p>I can think of no better way to close this gap than to get kids into wild areas where Nature does the teaching, affecting students in ways that stick with them for the rest of their lives."</p>
      <p class="byline">–Mara Elden, Explorer, Wildlife Biologist, Author</p>
    </div>
  </article>

  <article class="panel panel--research">
    <h2>Why is it important to spend time outdoors?</h2>
    <p class="lead">Well, here is what the research says!</p>
    <p>Regular contact with nature promotes healthier social behavior and lessens social dysfunction, helps alleviate stress, improves resilience, promotes optimal psychological functioning, improves recovery from physical trauma, and reduces mortality.</p>
    <p>A child's time in nature provides the benefits of creating sacred places, development of self and greater independence.</p>
    <p>Children with ADHD who regularly play in green settings have milder symptoms than children who play in built outdoor and indoor settings.</p>
    <p>School gardens positively impact children's learning and behavior.</p>
    <p>Pregnant women living in areas with more trees had better birth outcomes.</p>
    <p>Outdoor experience for teens has self-reported life-changing results.</p>
    <p>Children's emotional affinity towards nature is a strong predictor of their willingness to protect the environment.</p>
    <p class="note">All research summarized &amp; provided by the Kids Outdoors Alliance</p>
    <p class="url">http://www.kidsoutdoorsalliance.qz/</p>
    <p class="partner">Kids Outdoors Alliance</p>
    <div class="grass" role="img" aria-label="Band of green grass blades along the bottom edge"></div>
  </article>

  <article class="panel panel--ways">
    <h2>Ways to Get Outside!</h2>
    <p>With over 80% of Canadians living in urban areas, our feet are more familiar with concrete than they are with the forest floor. Canadians spend over 90% of their time indoors and on average, six or more hours a day in front of a screen. This disconnection from the natural world is called Nature Deficit Disorder and is correlated with the increased incidence of obesity, heart disease, asthma, depression, and stress.</p>
    <p>Fortunately, the antidote to this modern-day ailment is just beyond our front doors. Take time every day to take your vitamin O(utside)! Here is how:</p>
    <ul>
      <li>Explore the wild places in your neighborhood.</li>
      <li>Rediscover and reclaim your childhood wild places with your children.</li>
      <li>Commit to sitting still in nature daily for a minimum of 20 minutes, and then share this experience with others by telling them about your solo time.</li>
      <li>Find a local group that engages its members in outdoor recreation; meet new friends to get outdoors with!</li>
      <li>Discover the names and uses of local flora and fauna in your region by investing in a plant or animal guidebook.</li>
      <li>Get dirty, play in the mud, and jump in puddles!</li>
      <li>Use nature as inspiration to create art, or better yet make natural art installments outside – think Lena Brookfield!</li>
      <li>Create a garden, and enjoy the plethora of fruits born of this labor.</li>
    </ul>
    <svg class="circles" viewBox="0 0 230 78" aria-hidden="true">
      <rect x="60" y="32" width="110" height="14" fill="var(--white)"/>
      <circle cx="39" cy="39" r="37" fill="var(--white)"/>
      <circle cx="191" cy="39" r="37" fill="var(--white)"/>
      <circle cx="39" cy="39" r="31" fill="#6f8f5a" role="img" aria-label="Photo of students gathered on a grassy field"/>
      <circle cx="191" cy="39" r="31" fill="#a6a39a" role="img" aria-label="Photo of students in gear on a rocky shore"/>
    </svg>
  </article>
</section>

<section class="spread spread--inside" aria-label="Brochure inside">
  <article class="panel panel--program">
    <div class="strip strip--teal"></div>
    <header class="program-head">
      <h2>Wild Trails Leadership Program:</h2>
      <p class="quote">" I have never experienced a sensation like this before and at first, I could not put my finger on what it was, but then I realized it was bliss." – Priya (WTLP Alumni)</p>
      <p class="quote">"In finding the gifts and potential of others, we discover and unleash a deeper appreciation for ourselves."</p>
      <p class="quote-by">– Leah (WTLP Alumni)</p>
    </header>
    <div class="photo photo--sun" role="img" aria-label="Photo of students in a circle on grass, backlit by low sun"></div>
    <div class="program-body">
      <p>WTLP offers secondary students an applied field-course in Leadership Studies. During this 9-day summer outdoor immersion, students will develop their Action-Centered leadership skills. The climax of WTLP is the Journey, which is taken through a modality of choice (Riboard, Voyageur, SUP).</p>
      <p>WTLP is a transformative passage where learners develop a deeper relational understanding of themselves within the greater cultural and biological ecology of the Pacific Northwest.</p>
    </div>
    <div class="mini-brand"><span class="mark"></span>WTLP</div>
  </article>

  <article class="panel panel--program">
    <div class="strip strip--red"></div>
    <header class="program-head">
      <h2>Ridgeline Academy:</h2>
      <p class="quote">"Not only was the Ridgeline Academy program the most engaging educational experience, it also inspired me to look at my community and our environment in a profoundly new light.</p>
      <p class="quote-by">– Owen (RA Alumni)</p>
    </header>
    <div class="photo photo--dusk" role="img" aria-label="Photo of a group silhouetted against a sunset over water"></div>
    <div class="program-body">
      <p>The Ridgeline Academy (RA) is an enriched outdoor education program which focuses on character development through Leadership, Citizenship and Outdoor Adventure. This semester-long program offers students a unique opportunity to obtain high school credits, hard-skills, and outdoor certifications that prepare students for future careers and studies.</p>
      <p>The program often includes an international service project and a practicum delivering a overnight environmental education program for all grade seven students in the district.</p>
    </div>
  </article>

  <article class="panel panel--program">
    <div class="strip strip--yellow"></div>
    <header class="program-head">
      <h2>Green Action Workshop:</h2>
      <p class="quote">"Inspiration: It comes to me when I realize that big problems have simple solutions that are within reach and already exist."</p>
      <p class="quote-by">– Evan (GAW Alumni)</p>
    </header>
    <div class="photo photo--map" role="img" aria-label="Photo of hands plotting a course on a nautical chart with a ruler"></div>
    <div class="program-body">
      <p>The Coastal Metro Green Action Workshop is a unique and experience-based youth leadership program that brings together students who are passionate about influencing sustainability in their schools and school communities through action, collaboration, and leadership. This action-packed credit course takes includes a 8 day field camp in August and a number of weekend sessions throughout the fall.</p>
      <p>The course features a wide range of fun and experiential learning and leadership development opportunities designed to develop the knowledge and skills necessary to take action for sustainability.</p>
    </div>
  </article>
</section>

</body>
</html>
```